Flyer for DK Siren Installers

This flyer will help our technicians upsell/educate our current customers on the different service packages that we offer when the tech is in the customers home.

```html
<!DOCTYPE html>
<html lang="en">
<head>
<meta charset="utf-8">
<title>DK Siren Installers – Service Packages Flyer</title>
<link rel="stylesheet" href="https://fonts.googleapis.com/css2?family=Arimo:wght@400;700&family=Montserrat:wght@500;600;700;800&display=swap">
<style>
:root{
  --navy:#12428f;
  --navy-deep:#0d3170;
  --green:#3cb54a;
  --green-soft:#d9efd9;
  --grey-bar:#dcdcdc;
  --grey-box:#d6d6d6;
  --ink:#1d1d1d;
  --page:#efefef;
  --white:#ffffff;
}
*{box-sizing:border-box;margin:0;padding:0}
html,body{width:783px;height:1200px;overflow:hidden;background:var(--page)}
body{font-family:"Montserrat",sans-serif;color:var(--ink);position:relative}
.flyer{position:absolute;left:21px;top:77px;width:740px;height:1046px;background:var(--white);overflow:hidden;box-shadow:0 2px 10px rgba(0,0,0,.15)}
.hero{position:absolute;left:0;top:0;width:740px;height:425px}
.hero-bg{position:absolute;inset:0}
.brand{position:absolute;left:33px;top:30px;font-weight:800;font-size:36px;letter-spacing:1px;color:var(--navy);display:flex;align-items:center;gap:10px}
.brand-dot{width:14px;height:14px;border-radius:50%;background:var(--green)}
.headline{position:absolute;left:32px;top:118px;font-family:"Arimo",sans-serif;line-height:1}
.headline .pre{display:block;font-weight:400;font-size:38px;color:var(--white)}
.headline .robbed{display:block;font-weight:700;font-size:64px;color:var(--green);margin-top:6px}
.headline .twice{display:block;font-weight:700;font-size:82px;color:var(--white);margin-top:-2px}
.tagline{position:absolute;left:39px;top:343px;font-weight:700;font-size:16px;line-height:1.2;color:var(--white)}
.product-photo{position:absolute;left:385px;top:55px;width:355px;height:370px}
.package-note{position:absolute;left:31px;top:443px;width:674px;height:34px;background:var(--grey-bar);display:flex;align-items:center;justify-content:center;font-weight:600;font-size:10.5px;letter-spacing:.2px}
.accent{color:var(--navy)}
.device-row{position:absolute;left:31px;top:486px;width:674px;display:flex;gap:8px}
.device{width:129px}
.device-frame{height:104px;border:2px solid var(--green);display:flex;align-items:center;justify-content:center}
.device-label{margin-top:6px;height:24px;background:var(--green-soft);display:flex;align-items:center;justify-content:center;font-weight:600;font-size:9px}
.thumb{background:linear-gradient(160deg,#f2f2f2,#9a9a9a);border-radius:6px}
.pricing-row{position:absolute;left:31px;top:633px;width:674px;display:flex;gap:11px}
.pricing-note{width:160px;height:43px;background:var(--grey-box);display:flex;align-items:center;justify-content:center;padding:0 10px}
.pricing-note .note-text{display:block;text-align:center;font-weight:500;font-size:7.3px;line-height:1.3}
.package-row{position:absolute;left:31px;top:690px;width:674px;display:flex;gap:11px}
.package{width:160px;height:128px;border:2px solid var(--green);display:flex;flex-direction:column;align-items:center;justify-content:flex-start;padding-top:22px;text-align:center;font-weight:600;font-size:7.3px;line-height:1.25}
.package .thumb{margin-bottom:12px}
.package .fine{font-size:4.5px;font-weight:500;margin-top:4px}
.panel-box{justify-content:center;padding-top:0}
.options{position:absolute;left:31px;top:860px;width:500px;display:flex}
.option{width:245px;padding-right:20px;font-weight:700;font-size:13.5px;line-height:1.25}
.option + .option{border-left:1px solid #bdbdbd;padding-left:19px;padding-right:0;width:235px}
.option-title{display:block;color:var(--green);font-size:13.5px}
.kit-box{position:absolute;left:545px;top:829px;width:160px;height:127px;border:2px solid var(--green);display:flex;align-items:center;justify-content:center}
.footer{position:absolute;left:0;top:972px;width:740px;height:74px}
.footer-bg{position:absolute;inset:0}
.website{position:absolute;left:33px;top:1013px;display:flex;align-items:center;gap:13px;font-weight:700;font-size:15.5px;letter-spacing:1px}
.call{position:absolute;left:386px;top:997px;font-weight:700;font-size:18.5px;color:var(--white)}
.call .lead{color:var(--green);font-size:16px;margin-right:6px}
.contact{position:absolute;left:386px;top:1021px;display:flex;gap:10px;font-weight:600;font-size:8.5px;color:var(--white)}
.contact span{display:flex;align-items:center;gap:4px}
</style>
</head>
<body>
<main class="flyer">
  <section class="hero">
    <svg class="hero-bg" width="740" height="425" viewBox="0 0 740 425">
      <defs>
        <linearGradient id="heroBlue" x1="0" y1="0" x2="1" y2="1">
          <stop offset="0" stop-color="#174a96"/>
          <stop offset="1" stop-color="#0d3170"/>
        </linearGradient>
      </defs>
      <rect width="740" height="425" fill="url(#heroBlue)"/>
      <polygon points="0,0 330,0 300,88 0,88" fill="#fff"/>
      <polygon points="0,323 430,323 408,396 0,396" fill="#3cb54a"/>
      <polygon points="0,396 408,396 460,425 0,425" fill="#fff"/>
    </svg>
    <div class="brand"><span>DK Siren</span><span class="brand-dot"></span></div>
    <h1 class="headline"><span class="pre">DON’T GET</span><span class="robbed">ROBBED</span><span class="twice">TWICE</span></h1>
    <p class="tagline">We offer a more affordable home security &amp;<br>automation than what you currently have.</p>
    <div class="product-photo" role="img" aria-label="Product photo of doorbell cameras and an indoor camera" style="background:radial-gradient(ellipse at 55% 60%,#c9ccd1 0%,#5b6470 45%,rgba(13,49,112,0) 75%)"></div>
  </section>

  <p class="package-note">ONE HOME AUTOMATION DEVICE REQUIRES A&nbsp;<span class="accent">$6 A MONTH INCREASE PER DEVICE WITH A 60 MONTH RENEWAL</span></p>

  <section class="device-row">
    <div class="device"><div class="device-frame"><div class="thumb" role="img" aria-label="Doorbell cameras photo" style="width:70px;height:62px"></div></div><p class="device-label">DOOR BELL CAMERAS</p></div>
    <div class="device"><div class="device-frame"><div class="thumb" role="img" aria-label="Thermostat photo" style="width:80px;height:62px;background:linear-gradient(160deg,#fafafa,#d6d6d6)"></div></div><p class="device-label">HUB THERMOSTAT</p></div>
    <div class="device"><div class="device-frame"><div class="thumb" role="img" aria-label="Smart deadbolt locks photo" style="width:92px;height:66px;background:linear-gradient(160deg,#e8d9a0,#555)"></div></div><p class="device-label">AUTO DEADBOLT</p></div>
    <div class="device"><div class="device-frame"><div class="thumb" role="img" aria-label="Garage controller photo" style="width:80px;height:50px;background:linear-gradient(160deg,#555,#111)"></div></div><p class="device-label">GARAGE CONTROLLER</p></div>
    <div class="device"><div class="device-frame"><div class="thumb" role="img" aria-label="Indoor camera photo" style="width:46px;height:70px"></div></div><p class="device-label">INDOOR CAMERA</p></div>
  </section>

  <section class="pricing-row">
    <div class="pricing-note"><span class="note-text">Outdoor Camera Requires A <span class="accent">$12</span> A Month Increase For The Camera Per Camera</span></div>
    <div class="pricing-note"><span class="note-text">Doorbell Camera And An Outdoor Camera Requires A <span class="accent">$20</span> Increase A Month For Both These Devices:</span></div>
    <div class="pricing-note"><span class="note-text">Two Or More Outdoor Cameras Requires A <span class="accent">$12</span> Increase Per Month Per Outdoor Camera</span></div>
    <div class="pricing-note"><span class="note-text">Sentry 2 Panel Upgrade Requires A <span class="accent">$5</span> Increase Per Month With A 60 Month Renewal And A One Time Fee <span class="accent">$100</span></span></div>
  </section>

  <section class="package-row">
    <div class="package"><div class="thumb" role="img" aria-label="Outdoor camera photo" style="width:56px;height:34px"></div>OUTDOOR CAMERAS</div>
    <div class="package" style="padding-top:8px"><div class="thumb" role="img" aria-label="Outdoor camera and doorbell camera photo" style="width:62px;height:56px;margin-bottom:8px"></div>1 OUTDOOR CAMERA +<br>ONE OTHER DEVICE<br>(DOORBELL CAMERA)</div>
    <div class="package"><div class="thumb" role="img" aria-label="Two outdoor cameras photo" style="width:100px;height:34px"></div>2-4 OUTDOOR CAMERAS<br>+12 PER CAMERA<span class="fine">*Add $6 for 5-6 cameras, extra clip storage</span></div>
    <div class="package panel-box"><div class="thumb" role="img" aria-label="Security control panel photo" style="width:106px;height:72px;margin:0;background:linear-gradient(160deg,#f0f0f0,#8d939b)"></div></div>
  </section>

  <section class="options">
    <p class="option"><span class="option-title">1ST OPTION:</span>Phoneline To Cell Primary No App Requires <span class="accent">$7</span> Increase Per Month, Also Requires A 60 Month Renewal</p>
    <p class="option"><span class="option-title">2ND OPTION:</span>Phoneline To Cell Primary With App Requires A <span class="accent">$13</span> A Month Increase, Also Requires A 60 Month Renewal</p>
  </section>
  <div class="kit-box"><div class="thumb" role="img" aria-label="Cellular communicator module photo" style="width:100px;height:96px;background:linear-gradient(160deg,#e9e0d8,#2f4a3a)"></div></div>

  <footer class="footer">
    <svg class="footer-bg" width="740" height="74" viewBox="0 0 740 74">
      <polygon points="344,0 740,0 740,74 314,74" fill="#12428f"/>
      <polygon points="355,0 369,0 339,64 325,64" fill="#3cb54a"/>
      <rect x="0" y="70" width="740" height="4" fill="#12428f"/>
    </svg>
  </footer>
  <p class="website">
    <svg width="18" height="18" viewBox="0 0 18 18" aria-hidden="true"><g fill="none" stroke="#3cb54a" stroke-width="1.6"><circle cx="9" cy="9" r="7.5"/><ellipse cx="9" cy="9" rx="3.2" ry="7.5"/><line x1="1.5" y1="9" x2="16.5" y2="9"/><line x1="3" y1="5" x2="15" y2="5"/><line x1="3" y1="13" x2="15" y2="13"/></g></svg>
    WWW.dksirenhome.com
  </p>
  <p class="call"><span class="lead">CALL US NOW:</span>888-555-0142</p>
  <p class="contact">
    <span><svg width="10" height="8" viewBox="0 0 10 8" aria-hidden="true"><rect x=".5" y=".5" width="9" height="7" fill="none" stroke="#3cb54a"/><polyline points=".5,.5 5,4.5 9.5,.5" fill="none" stroke="#3cb54a"/></svg>info@dksirenhome.com</span>
    <span><svg width="7" height="10" viewBox="0 0 7 10" aria-hidden="true"><path d="M3.5 10 C1 6 0 5 0 3.5 A3.5 3.5 0 0 1 7 3.5 C7 5 6 6 3.5 10Z" fill="#3cb54a"/><circle cx="3.5" cy="3.5" r="1.3" fill="#12428f"/></svg>PO Box 2210. Maple Grove, WA 98000</span>
  </p>
</main>
</body>
</html>
```